" SOMOS UM CONSULTÓRIO ODONTOLÓGICO, QUE TRABALHA COM IMPLANTES DENTÁRIOS E APARELHOS ORTODÔNTICOS, VISANDO SEMPRE O CONFORTO E SAÚDE DOS NOSSOS PACIENTES, "

```html
<!DOCTYPE html>
<html lang="pt-BR">
<head>
<meta charset="utf-8">
<title>Sorriso Pleno – Cartões de visita</title>
<link rel="stylesheet" href="https://fonts.googleapis.com/css2?family=Didact+Gothic&family=Open+Sans:wght@400;600&display=swap">
<style>
  :root {
    --bg: #eef0f3;
    --white: #ffffff;
    --navy: #1f3670;
    --blue: #33569a;
    --blue-light: #4a73b8;
    --sky: #7cc3e8;
    --text-dark: #1d2433;
    --teal: #2a8fb8;
    --line: rgba(255,255,255,0.55);
  }
  * { box-sizing: border-box; margin: 0; padding: 0; }
  html, body { width: 1200px; height: 1200px; overflow: hidden; }
  body {
    background: var(--bg);
    font-family: "Open Sans", sans-serif;
    position: relative;
  }
  .card {
    position: absolute;
    left: 280px;
    width: 640px;
    height: 366px;
    border-radius: 22px;
    overflow: hidden;
    box-shadow: 0 10px 30px rgba(20,35,70,0.18);
  }
  /* Front */
  .card-front { top: 90px; background: var(--white); }
  .brand {
    position: absolute; left: 0; right: 0;
    display: flex; flex-direction: column; align-items: center;
  }
  .card-front .brand { top: 40px; }
  .brand-mark {
    width: 62px; height: 62px; border-radius: 50%;
    background: var(--teal); margin-bottom: 12px;
  }
  .brand-name {
    font-family: "Didact Gothic", sans-serif;
    font-size: 56px; line-height: 1; color: var(--teal);
    letter-spacing: 0.5px;
  }
  .brand-tagline {
    font-size: 12px; letter-spacing: 4px; color: var(--teal);
    margin-top: 8px; text-transform: uppercase;
  }
  .services {
    position: absolute; top: 228px; left: 0; right: 0;
    text-align: center; font-size: 17px; font-weight: 600; color: var(--text-dark);
  }
  .front-band {
    position: absolute; left: 0; right: 0; bottom: 0; height: 82px;
    background: linear-gradient(180deg, var(--blue-light), var(--navy));
    border-top: 6px solid var(--sky);
    display: flex; align-items: center; padding-left: 44px;
    color: var(--white); font-size: 22px;
  }
  /* Back */
  .card-back {
    top: 490px;
    background: radial-gradient(ellipse at 75% 40%, var(--blue-light), var(--blue) 45%, var(--navy));
    border-bottom: 8px solid var(--sky);
    color: var(--white);
  }
  .person { position: absolute; left: 44px; top: 38px; }
  .person-name { font-size: 26px; font-weight: 400; }
  .person-reg { font-size: 13px; opacity: 0.85; margin-top: 2px; }
  .contacts { position: absolute; left: 44px; top: 128px; list-style: none; }
  .contact {
    display: flex; align-items: flex-start; gap: 14px;
    margin-bottom: 16px; font-size: 14px; line-height: 1.45;
  }
  .contact-icon {
    flex: none; width: 26px; height: 26px; border-radius: 50%;
    background: var(--white); display: flex; align-items: center; justify-content: center;
  }
  .divider {
    position: absolute; left: 372px; top: 40px; width: 1px; height: 260px;
    background: var(--line);
  }
  .card-back .brand { left: 372px; top: 100px; }
  .card-back .brand-mark { background: var(--white); }
  .card-back .brand-name { color: var(--white); font-size: 44px; }
  .card-back .brand-tagline { color: var(--white); opacity: 0.8; font-size: 10px; letter-spacing: 3px; }
  /* Logo lockup */
  .logo-lockup { position: absolute; left: 0; right: 0; top: 920px; }
  .logo-lockup .brand { position: static; }
</style>
</head>
<body>
  <section class="card card-front" aria-label="Frente do cartão">
    <div class="brand">
      <span class="brand-mark"></span>
      <span class="brand-name">Sorriso Pleno</span>
      <span class="brand-tagline">Odontologia Especializada</span>
    </div>
    <p class="services">Implantodontia - ortodontia - estética</p>
    <div class="front-band">drmvlopes@mail.com</div>
  </section>

  <section class="card card-back" aria-label="Verso do cartão">
    <div class="person">
      <p class="person-name">Marcos Vieira Lopes</p>
      <p class="person-reg">Cro - Mt 4826</p>
    </div>
    <ul class="contacts">
      <li class="contact">
        <span class="contact-icon">
          <svg width="14" height="14" viewBox="0 0 24 24"><path fill="#1f3670" d="M6.6 10.8a15 15 0 0 0 6.6 6.6l2.2-2.2a1 1 0 0 1 1-.25 11.4 11.4 0 0 0 3.6.57 1 1 0 0 1 1 1V20a1 1 0 0 1-1 1A17 17 0 0 1 3 4a1 1 0 0 1 1-1h3.5a1 1 0 0 1 1 1c0 1.25.2 2.45.57 3.57a1 1 0 0 1-.25 1z"/></svg>
        </span>
        <span>(66) 3400-1234<br>(66) 9200-5678<br>(66) 9900-4321</span>
      </li>
      <li class="contact">
        <span class="contact-icon">
          <svg width="14" height="14" viewBox="0 0 24 24"><circle cx="12" cy="12" r="4" fill="none" stroke="#1f3670" stroke-width="2.4"/><path d="M16 12v1.5a2.5 2.5 0 0 0 5 0V12a9 9 0 1 0-4 7.5" fill="none" stroke="#1f3670" stroke-width="2.4"/></svg>
        </span>
        <span>drmvlopes@mail.com<br>sorrisopleno.com.br</span>
      </li>
      <li class="contact">
        <span class="contact-icon">
          <svg width="14" height="14" viewBox="0 0 24 24"><path fill="#1f3670" d="M12 2a7 7 0 0 0-7 7c0 5.25 7 13 7 13s7-7.75 7-13a7 7 0 0 0-7-7zm0 9.5A2.5 2.5 0 1 1 12 6.5a2.5 2.5 0 0 1 0 5z"/></svg>
        </span>
        <span>Rua das Acácias, 120 - Centro<br>Vila Serena</span>
      </li>
    </ul>
    <div class="divider"></div>
    <div class="brand" style="right:0">
      <span class="brand-mark"></span>
      <span class="brand-name">Sorriso Pleno</span>
      <span class="brand-tagline">Odontologia Especializada</span>
    </div>
  </section>

  <section class="logo-lockup" aria-label="Marca">
    <div class="brand">
      <span class="brand-mark"></span>
      <span class="brand-name">Sorriso Pleno</span>
      <span class="brand-tagline">Odontologia Especializada</span>
    </div>
  </section>
</body>
</html>
```